Stonebridge 720 Real Estate Investment Company

We need a business card designed for a real estate investment company named Stonebridge 720. We want to use red#f04a50, orange #f37122 and yellow #fbee3e as the color scheme. The logo colors will need to be modified from the current blue palette. I've attach VitalBranchly logo example that captures the color scheme we're going for for Stonebridge 720. Looking for clean Sans Serif fonts.
Contact Information for Business Card
Daniel Whitlock
Managing Partner
48613 Kessler Lane, Suite 540
Cedar Vale, OH 44291
330-555-8740 Mobile
dwhitlock@stonebridge720.example
www.stonebridge720.example
Requirements
Must have
- Looking for creative responses.
Nice to have
- Must hit color palette... orange, red, yellow

```html
<!DOCTYPE html>
<html lang="en">
<head>
<meta charset="utf-8">
<title>Stonebridge 720 – Business Card</title>
<link href="https://fonts.googleapis.com/css2?family=Montserrat:wght@400;500;800&display=swap" rel="stylesheet">
<style>
  :root {
    --red: #f04a50;
    --orange: #f37122;
    --yellow: #fbee3e;
    --ink: #2b2b2b;
    --paper: #ffffff;
    --backdrop: #e3e3e8;
  }
  * { box-sizing: border-box; margin: 0; padding: 0; }
  html, body { width: 1200px; height: 1000px; overflow: hidden; }
  body {
    background: var(--backdrop);
    font-family: "Montserrat", Arial, sans-serif;
    position: relative;
  }
  .card {
    position: absolute;
    left: 250px;
    width: 700px;
    height: 400px;
    background: var(--paper);
    box-shadow: 0 6px 18px rgba(0,0,0,.08);
  }
  .card--front { top: 70px; }
  .card--back { top: 530px; }

  .brand {
    position: absolute;
    display: flex;
    align-items: center;
    gap: 12px;
  }
  .brand__dot {
    width: 18px; height: 18px;
    border-radius: 50%;
    background: var(--orange);
    flex: none;
  }
  .brand__name {
    font-weight: 800;
    color: var(--red);
    font-size: 40px;
    letter-spacing: -0.5px;
    white-space: nowrap;
  }
  .card--front .brand { right: 44px; top: 56px; }

  .person { position: absolute; left: 48px; top: 150px; }
  .person__name {
    font-weight: 500;
    font-size: 34px;
    color: var(--ink);
    letter-spacing: 0.5px;
  }
  .person__title {
    margin-top: 4px;
    font-size: 14px;
    color: var(--red);
    letter-spacing: 2.5px;
    text-transform: uppercase;
  }

  .contact {
    position: absolute;
    right: 44px;
    bottom: 40px;
    list-style: none;
    text-align: right;
    font-size: 15px;
    color: var(--ink);
    line-height: 1.55;
    letter-spacing: 0.4px;
  }
  .contact__item { display: flex; justify-content: flex-end; align-items: flex-start; gap: 12px; white-space: nowrap; }
  .contact__icon { width: 16px; height: 16px; flex: none; margin-top: 4px; fill: var(--red); }
  .contact__spacer { width: 16px; flex: none; }

  .card--back .brand { left: 140px; top: 130px; }
  .card--back .brand__name { font-size: 46px; }
  .back__url {
    position: absolute;
    left: 140px;
    top: 230px;
    font-size: 20px;
    color: var(--red);
    letter-spacing: 1.5px;
  }
</style>
</head>
<body>

<section class="card card--front">
  <div class="brand">
    <span class="brand__dot"></span>
    <span class="brand__name">Stonebridge 720</span>
  </div>

  <div class="person">
    <div class="person__name">Daniel Whitlock</div>
    <div class="person__title">Managing Partner</div>
  </div>

  <ul class="contact">
    <li class="contact__item">330-555-8740
      <svg class="contact__icon" viewBox="0 0 24 24" aria-hidden="true"><path d="M6.6 10.8a15.1 15.1 0 0 0 6.6 6.6l2.2-2.2a1 1 0 0 1 1-.25 11.4 11.4 0 0 0 3.6.6 1 1 0 0 1 1 1V20a1 1 0 0 1-1 1A17 17 0 0 1 3 4a1 1 0 0 1 1-1h3.5a1 1 0 0 1 1 1c0 1.25.2 2.45.6 3.6a1 1 0 0 1-.25 1z"/></svg>
    </li>
    <li class="contact__item">dwhitlock@stonebridge720.example
      <svg class="contact__icon" viewBox="0 0 24 24" aria-hidden="true"><path d="M2 5h20v14H2z M4 7v.4l8 5 8-5V7l-8 5z" fill-rule="evenodd"/></svg>
    </li>
    <li class="contact__item">www.stonebridge720.example
      <svg class="contact__icon" viewBox="0 0 24 24" aria-hidden="true"><path d="M12 2a10 10 0 1 0 0 20 10 10 0 0 0 0-20zm0 2c.9 0 2.1 1.8 2.6 5H9.4C9.9 5.8 11.1 4 12 4zM4.3 10h3c-.1.7-.1 1.3-.1 2s0 1.3.1 2h-3a8 8 0 0 1 0-4zm4.9 0h5.6c.1.6.1 1.3.1 2s0 1.4-.1 2H9.2c-.1-.6-.1-1.3-.1-2s0-1.4.1-2zm7.5 0h3a8 8 0 0 1 0 4h-3c.1-.7.1-1.3.1-2s0-1.3-.1-2zM9.4 15h5.2c-.5 3.2-1.7 5-2.6 5s-2.1-1.8-2.6-5z"/></svg>
    </li>
    <li class="contact__item">48613 Kessler Lane, Suite 540
      <svg class="contact__icon" viewBox="0 0 24 24" aria-hidden="true"><path d="M12 2a7 7 0 0 0-7 7c0 5 7 13 7 13s7-8 7-13a7 7 0 0 0-7-7zm0 9.5A2.5 2.5 0 1 1 12 6.5a2.5 2.5 0 0 1 0 5z"/></svg>
    </li>
    <li class="contact__item">Cedar Vale, OH&nbsp; 44291<span class="contact__spacer"></span></li>
  </ul>
</section>

<section class="card card--back">
  <div class="brand">
    <span class="brand__dot"></span>
    <span class="brand__name">Stonebridge 720</span>
  </div>
  <div class="back__url">www.stonebridge720.example</div>
</section>

</body>
</html>
```